Award Winning Novel Needs a Cover Facelift

I would like a designer to provide a cutting-edge designed book cover for award-winning novel, "Paper Lanterns".
Book dimensions:
5.5 x 8.5, spine .75 inches, 290 pages
I currently have a cover I'm happy with but it needs to appeal to a broader audience. Please use the current cover as a foundation. I have also included pics of books that are in my genre that I like.

This is a middle-grade novel (kids ages 9 to 13) about an eleven-year-old girl who deals with the challenges of being a military brat. She is of mixed race (partially Japanese and African American). Keira dreams of belonging...specifically she wants to join the competitive neighborhood swim team (Marlins). She believes that participating on the team will be her way of making friends, and helping her to one day fulfill a dream of becoming an Valdoran swimmer. That dream is challenged when she realizes she's the worst on the team. She also deals with worrying about her mother dying in the Middle East.
With all that being said, I need a cover that will make a middle grade kid want to pick up the book and read it. It should not look to childish but still feel kid friendly. The current font I actually like and I purchased it on typevault.example
The font is very important to making this current cover phenomenal.

Themes include:
-Competitive swimming (teamwork)
-Family
-Community
-Military Families (more global than just U.S.)
-Neighborhood
-Overcoming Fears
-Friendship
-Nature (walkable communities, there are lots of bridges in the community)
-Hummingbirds (This theme is a symbol...they are everywhere in her new community...her mom gives her a hummingbird necklace before she leaves for her deployment...they have Paper Lanterns...they travel long distances...they appear almost fearless to be so small)
-Multi-culturalism/diversity
-Hope
-Hypocrisy

Please note that I want the new design to include the book side panels/side book flaps. Please use temporary image. I have also included images of other book covers I like as well as a sample of the soft cover that will go with the hardcover.

Don't be limited by what I have provided. I love this current design but I'm striving for the best look.

Target Market(s)

Preteens and teen (9-15)

Requirements
Must have
• great fonts, tiny humminbirds, something that represents swimming, water

```html
<!DOCTYPE html>
<html lang="en">
<head>
<meta charset="utf-8">
<title>Paper Lanterns – Book Cover Wrap</title>
<link rel="stylesheet" href="https://fonts.googleapis.com/css2?family=Bangers&family=Anton&family=EB+Garamond&display=swap">
<style>
  :root {
    --ink: #0a0d1a;
    --back-blue: #66adf3;
    --back-light: #ffffff;
    --spine: #8edcf9;
    --front-bg: #fdfdf6;
    --water: #2f7fd8;
    --water-deep: #1a4fb8;
    --teal: #1f8c86;
    --bird-red: #e23a5c;
    --white: #ffffff;
  }
  * { margin: 0; padding: 0; box-sizing: border-box; }
  html, body { width: 1200px; height: 868px; overflow: hidden; background: #ffffff; }
  .cover-wrap { position: relative; width: 1200px; height: 868px; overflow: hidden; }

  /* Back cover */
  .back-cover {
    position: absolute; left: 0; top: 0; width: 562px; height: 868px;
    background: linear-gradient(35deg, var(--back-blue) 0%, #a9d2f7 40%, #e6f1fd 70%, var(--back-light) 100%);
  }
  .back-blurb {
    position: absolute; left: 70px; top: 76px; width: 431px;
    font-family: "EB Garamond", serif; font-size: 15.6px; line-height: 20.4px;
    color: #1c1c1c; text-align: justify;
  }
  .back-blurb p + p { margin-top: 20px; }
  .back-title {
    position: absolute; left: 120px; top: 488px; width: 340px; text-align: center;
    font-family: "Bangers", sans-serif; color: var(--ink); line-height: 0.9;
  }
  .back-title .line-main { display: block; font-size: 96px; letter-spacing: 1px; }
  .back-title .line-sub { display: block; font-size: 62px; letter-spacing: 1px; }
  .isbn-box { position: absolute; left: 58px; top: 707px; width: 131px; height: 116px; background: var(--white); }

  /* Spine */
  .spine {
    position: absolute; left: 562px; top: 0; width: 76px; height: 868px; background: var(--spine);
  }
  .spine-title, .spine-author {
    position: absolute; left: 50%; white-space: nowrap; color: var(--ink);
    transform-origin: center; transform: translate(-50%, -50%) rotate(-90deg);
  }
  .spine-title { top: 180px; font-family: "Bangers", sans-serif; font-size: 40px; letter-spacing: 1px; }
  .spine-author { top: 670px; font-family: "Anton", sans-serif; font-size: 28px; letter-spacing: 9px; }

  /* Front cover */
  .front-cover {
    position: absolute; left: 638px; top: 0; width: 562px; height: 868px; background: var(--front-bg);
  }
  .front-art {
    position: absolute; left: 8px; top: 180px; width: 554px; height: 560px;
    border-radius: 46% 40% 44% 50%;
    background:
      radial-gradient(circle at 72% 30%, rgba(226,58,92,0.85) 0 14%, transparent 30%),
      radial-gradient(circle at 88% 80%, rgba(226,58,92,0.8) 0 10%, transparent 24%),
      radial-gradient(circle at 30% 20%, rgba(226,58,92,0.7) 0 9%, transparent 22%),
      radial-gradient(circle at 50% 60%, var(--teal) 0 16%, var(--water-deep) 34%, var(--water) 52%, rgba(140,200,245,0.5) 68%, transparent 78%);
  }
  .front-title {
    position: absolute; left: 40px; top: 6px; width: 510px; text-align: center;
    font-family: "Bangers", sans-serif; color: var(--ink); line-height: 0.88;
  }
  .front-title .line-main { display: block; font-size: 160px; letter-spacing: 2px; }
  .front-title .line-sub { display: block; font-size: 82px; letter-spacing: 2px; margin-left: 40px; }
  .front-author {
    position: absolute; left: 0; top: 742px; width: 562px; text-align: center;
    font-family: "Anton", sans-serif; font-size: 84px; color: var(--white); letter-spacing: 1px;
    text-shadow: 0 0 14px rgba(0,0,0,0.75), 0 0 4px rgba(0,0,0,0.5);
  }
</style>
</head>
<body>
<main class="cover-wrap">
  <section class="back-cover">
    <div class="back-blurb">
      <p>Lorem ipsum dolor sit amet, consectetur adipiscing elit. Cras eleifend dignissim ligula vel pretium. In eget nulla vel risus volutpat ultricies. Morbi nunc velit, ullamcorper non ipsum ut, congue consequat velit. Morbi lobortis faucibus nisl, vitae porttitor ex semper quis. Suspendisse ac purus nulla. Proin sagittis porttitor aliquet. Suspendisse malesuada est tellus, non scelerisque justo fermentum eu. Aenean ut pellentesque elit.</p>
      <p>Phasellus metus tellus, lacinia quis vestibulum nec, aliquet vitae ipsum. Curabitur tellus justo, facilisis eget elementum quis, varius in erat. Mauris facilisis, ligula eu facilisis feugiat, augue odio malesuada felis, eu pulvinar justo ante et massa. Suspendisse in mattis nulla, ac pellentesque metus. Phasellus dignissim feugiat risus, et hendrerit neque accumsan in. Donec tristique tincidunt justo eget faucibus. Praesent mattis auctor pulvinar. In velit enim, mollis vel eros ac, sollicitudin egestas tortor. Nam id ultricies erat. Nunc at elementum magna.</p>
    </div>
    <h2 class="back-title"><span class="line-main">PAPER</span><span class="line-sub">LANTERNS</span></h2>
    <div class="isbn-box"></div>
  </section>

  <section class="spine">
    <div class="spine-title">PAPER LANTERNS</div>
    <div class="spine-author">RENA MOSLEY</div>
  </section>

  <section class="front-cover">
    <div class="front-art" role="img" aria-label="Watercolour illustration of a young swimmer in goggles diving through a splash of blue water, surrounded by bright red and violet hummingbirds"></div>
    <h1 class="front-title"><span class="line-main">PAPER</span><span class="line-sub">LANTERNS</span></h1>
    <div class="front-author">RENA MOSLEY</div>
  </section>
</main>
</body>
</html>
```